Etiketten-Design für Honiggläser
Die Zusammenarbeit mit Jorin war sehr unkompliziert. Änderungswünsche wurden prompt umgesetzt und die Beratung war hervorragend! Besten Dank für das tolle Etikett!
Zielgruppe
Wir sind Imker und benötigen Etiketten für Honiggläser.
Aufgabenstellung
Siehe Anlage. Es sollen keine Fotos verwendet werden. Grafiken sind in Ordnung.
Etiketten-Design für Honigglas Etiketten-Design für Honigglas"
Format: Etikett für 250-gr.-Honigglas (TO ∅ 63 mm). Standardmaßgrösse 165 × 40 mm Design: schlicht, hochwertig, modern, edel/royal, unkonventionelles Design (weg von Bienen, Waben, Landschaften usw.), dunkle Farbtöne in Kontrast zu heller Schrift, die beiden Textbausteine 'Los Nr. ' sowi..
Attraktives Etiketten-Design für Honig Attraktives Etiketten-Design für Honig"
Wir verkaufen zur Zeit vor allem Waldhonig, streben aber auch einen Blütenhonig an. Das Etikett soll daher entweder den Wald wiederspiegeln oder aber neutral sein, so dass der Schriftzug Waldhonig oder Blütenhonig jeweils eingesetzt werden kann. Wichtig ist mir der Ortszusatz 'aus dem Glottertal..
Etiketten-Design für Produkte eines Familienbetriebs mit Imkerei und Hühnerhaltung Etiketten-Design für Produkte eines Familienbetriebs mit Imkerei und Hühnerhaltung"
1. Zentrale, auf allen Etiketten wiederkehrende Elemente: - Unser Riegelhaus (stilisiert) (Bild beiliegend) - Das Wort 'Weidlek' (Anmerkung: ohne Anführungszeichen) - die zentralen Elemente sollen die Produkte nicht überragen. 2. Dezente Adresse: - Familie Rattinger, Mühlgrund, CH-9617 Brüsel 3...
Etiketten-Design für Kurkuma-Honig Etiketten-Design für Kurkuma-Honig"
Etikett für 500g // Stanze eckig (210x35mm), Druckdatei entsprechend Vorgaben https://klebwerkstatt.de/faq/ Vorgaben für das Grünfeld Logo im Anhang Vorgaben für EG Öko Logo : https://oekosiegel-muster.eu/landbau/organic/downloads/logo_de Pflichtangaben auf dem Etikett: Gewicht, Adresse siehe Beispiel..
Etiketten-Design für Blütenhonig und Waldhonig gesucht Etiketten-Design für Blütenhonig und Waldhonig gesucht"
Zwei verschiedene Etiketten-Desings 1 x Blütenhonig sowie 1 x Waldhonig für unterschiedliche Honigglasgrößen (500 g und 250 g) Die Maße für die Etiketten wären: Für 500-Gramm-Glas 210 mm x 45 mm für's 250-Gramm-Glas 180 mm x 38 mm. Wir sind auch offen für neue Vorschläge bezüglich ..

```html
<!DOCTYPE html>
<html lang="de">
<head>
<meta charset="utf-8">
<title>Moosfelder Honig – Frühtracht Etikett</title>
<link href="https://fonts.googleapis.com/css2?family=Great+Vibes&family=Oswald:wght@300;400&display=swap" rel="stylesheet">
<style>
  :root {
    --paper: #ffffff;
    --black: #0d0d0d;
    --charcoal: #2a2a2a;
    --graphite: #5e5e5e;
    --gold: #d9a441;
    --honey: #d9b84a;
    --ink-light: #ffffff;
    --note-box: #f1f1ef;
  }
  * { margin: 0; padding: 0; box-sizing: border-box; }
  html, body { width: 1025px; height: 1200px; overflow: hidden; background: var(--paper); }
  .canvas { position: relative; width: 1025px; height: 1200px; overflow: hidden; }

  /* Deckel-Etikett */
  .lid-label {
    position: absolute; left: 304px; top: -3px; width: 422px; height: 422px;
    border-radius: 50%; overflow: hidden;
    border: 14px solid var(--gold);
    background: radial-gradient(circle at 55% 35%, var(--graphite) 0%, var(--charcoal) 45%, var(--black) 90%);
  }
  .lid-name {
    position: absolute; left: 0; right: 0; top: 78px; text-align: center;
    font-family: "Oswald", sans-serif; font-weight: 400; font-size: 40px;
    line-height: 48px; letter-spacing: 3px; color: var(--ink-light);
  }
  .lid-bee {
    position: absolute; left: 52px; top: 195px; width: 290px; height: 180px;
    border-radius: 50%;
    background: radial-gradient(ellipse at 50% 50%, #2a2515 0%, #d9d7d0 45%, rgba(230,230,225,0.25) 75%, transparent 80%);
  }

  /* Halsstreifen */
  .neck-strip {
    position: absolute; left: 424px; top: 400px; width: 183px; height: 371px;
    border-radius: 0 0 6px 6px;
    background: linear-gradient(90deg, #1b1b1b 0%, #0b0b0b 35%, #262626 100%);
  }

  /* Hauptetikett */
  .body-label { position: absolute; left: 0; top: 769px; width: 1025px; height: 431px; overflow: hidden; }
  .body-comb {
    position: absolute; inset: 0;
    background:
      radial-gradient(ellipse at 52% 35%, rgba(110,110,110,0.9) 0%, rgba(40,40,40,0.5) 35%, transparent 60%),
      linear-gradient(90deg, #2a2416 0%, #5a4a22 10%, #1c1a15 25%, #222 50%, #1c1a15 68%, #5a4a22 82%, #2a2416 100%);
  }
  .variety {
    position: absolute; left: 421px; width: 200px; top: 838px; text-align: center;
    font-family: "Oswald", sans-serif; font-weight: 300; font-size: 19px; letter-spacing: 1px;
    color: var(--ink-light);
  }
  .variety-name {
    position: absolute; left: 338px; top: 868px;
    font-family: "Great Vibes", cursive; font-size: 108px; line-height: 1;
    color: var(--ink-light); transform: rotate(-5deg);
  }
  .body-bee {
    position: absolute; left: 423px; top: 985px; width: 312px; height: 190px;
    border-radius: 50%;
    background: radial-gradient(ellipse at 50% 50%, #1e1b12 0%, #d8d6cf 40%, rgba(230,230,225,0.3) 70%, transparent 78%);
  }
  .side-text {
    position: absolute; writing-mode: vertical-rl; transform: rotate(180deg);
    font-family: "Oswald", sans-serif; font-weight: 300; color: var(--ink-light);
    font-size: 15px; line-height: 24.5px; letter-spacing: 1.2px; white-space: nowrap;
  }
  .side-text span { display: block; }
  .side-text--info { left: 38px; top: 795px; height: 381px; }
  .side-text--producer { left: 868px; top: 787px; height: 391px; letter-spacing: 1.6px; }
  .side-text--weight { left: 990px; top: 900px; height: 278px; letter-spacing: 1.6px; }
  .date-field {
    position: absolute; left: 967px; top: 794px; width: 43px; height: 132px;
    background: var(--note-box);
  }
</style>
</head>
<body>
<div class="canvas">

  <div class="lid-label">
    <div class="lid-name">MOOSFELDER<br>HONIG</div>
    <div class="lid-bee" role="img" aria-label="Illustration einer Biene mit Blüten"></div>
  </div>

  <div class="neck-strip"></div>

  <section class="body-label">
    <div class="body-comb" role="img" aria-label="Goldenes Wabenmuster auf dunklem Grund"></div>
  </section>

  <div class="variety">Blütenhonig cremig</div>
  <div class="variety-name">Frühtracht</div>
  <div class="body-bee" role="img" aria-label="Illustration einer Biene mit Blüten"></div>

  <div class="side-text side-text--info">
    <span>Bienenhonig kristallisiert bei längerer Lagerung. Durch</span>
    <span>Erwärmen im Wasserbad bei 40° C kann Honig ohne</span>
    <span>Schaden wieder verflüssigt werden.</span>
    <span>Ursprungsland: Deutschland, Bayern</span>
  </div>

  <div class="side-text side-text--producer">
    <span>Imkerei Brandauer Lindenweg 12, 85417 Moosfelden</span>
    <span>info@imkerei-brandauer.de</span>
    <span>Kühl, dunkel und trocken lagern.</span>
    <span>Mehrwegglas - Bitte zurück zum Imker</span>
  </div>

  <div class="side-text side-text--weight">
    <span>Blütenhonig 500g &nbsp;&nbsp;Haltbar bis:</span>
  </div>

  <div class="date-field"></div>

</div>
</body>
</html>
```